Web form face-lift for an online startup

We are a web startup building a SaaS application for the freight industry. The project is mainly dedicated to the paint the main form that our customer are using along the search results that the they get. All details are in the attached documents.
Updates
The application serves the Freight Forwarders community so please think towards this industry when using background images, banners, colors, icons, etc. Computer and technology images are irrelevant.
Customer fields at the top of the page is actually part of the form.
Target Market(s)
Usually business users (Sales people, procurement, shippers, freight forwarders). Some are less tech savvy and some appreciate the new trendy web apps.
Industry/Entity Type
Building
Colors
Designer to choose colors to be used in the design.
Look and feel
Each slider illustrates characteristics of the customer's brand and the style your logo design should communicate.

```html
<!DOCTYPE html>
<html lang="en">
<head>
<meta charset="utf-8">
<title>Freight Quote Results</title>
<link rel="stylesheet" href="https://fonts.googleapis.com/css2?family=Open+Sans:wght@400;600;700&display=swap">
<style>
:root{
  --blue:#0d6aad;
  --blue-dark:#0a4f85;
  --link:#2a9be0;
  --cta:#1aa3ee;
  --green:#7cbd66;
  --panel:#efefef;
  --panel-line:#d6d6d6;
  --text:#222;
  --muted:#888;
  --footer:#2e3133;
  --icon:#b5b5b5;
}
*{box-sizing:border-box;margin:0;padding:0}
html,body{width:1200px;height:1147px;overflow:hidden;background:#fff}
body{font-family:"Open Sans",Arial,sans-serif;color:var(--text)}
.stage{position:relative;width:1280px;height:1223px;transform:scale(.9375);transform-origin:0 0}
.abs{position:absolute}
a{color:var(--link);text-decoration:none}

.topbar{left:0;top:0;width:1280px;height:26px;background:#050505;color:#ddd;font-size:11px}
.topbar span{position:absolute;top:7px}
.header{left:0;top:26px;width:1280px;height:64px;background:var(--blue)}
.brand{left:170px;top:0;width:136px;height:64px;background:linear-gradient(#0e5d99,#094577);color:#fff;font-weight:700;font-size:23px;display:flex;align-items:center;justify-content:center;letter-spacing:.5px}
.menu{left:710px;top:0;display:flex;height:64px}
.menu a{width:80px;border-left:1px solid #0a5791;color:#cfe3f3;font-size:11.5px;display:flex;align-items:center;justify-content:center}
.menu a:last-child{border-right:1px solid #0a5791}
.menu a.active{color:#fff;font-weight:600}

.panel{background:var(--panel);border:1px solid var(--panel-line);box-shadow:0 1px 2px rgba(0,0,0,.12)}
.formbar{left:169px;top:104px;width:940px;height:76px}
.field{position:absolute;top:18px}
.field b{display:block;font-size:14px;font-weight:600}
.field small{display:block;font-size:10.5px;color:#999;margin-top:4px}
.field.sep{border-left:1px solid #d3d3d3;padding-left:20px;height:32px}
.btn-change{position:absolute;left:811px;top:17px;width:111px;height:39px;background:linear-gradient(#fff,#ececec);border:1px solid #ccc;border-radius:3px;font-size:15px;color:#666;display:flex;align-items:center;justify-content:center}

.filters{left:169px;top:206px;width:142px;height:406px;padding:22px 15px}
.filters h3{font-size:15px;font-weight:400;margin-bottom:10px}
.check{display:flex;align-items:center;font-size:11px;height:28px}
.box{width:16px;height:16px;background:#9a9a9a;border-radius:2px;margin-right:8px;display:inline-flex;align-items:center;justify-content:center;flex:none}
.box.on{background:#ddd;border:1px solid #bbb}
.filters hr{border:0;border-top:1px solid #d3d3d3;margin:14px 0 20px}
.range{position:relative;height:14px;margin-top:14px}
.range .track{position:absolute;left:0;right:0;top:5px;height:4px;background:#ddd;border-radius:2px}
.range .fill{position:absolute;left:20px;right:33px;top:5px;height:4px;background:var(--cta)}
.range .knob{position:absolute;top:0;width:13px;height:13px;border-radius:50%;background:#fff;border:1px solid #aaa}
.range-labels{display:flex;justify-content:space-between;font-size:11px;color:#999;margin-top:6px}

.btn-send{left:329px;top:205px;width:286px;height:42px;background:var(--cta);color:#fff;font-weight:600;font-size:15px;border-radius:3px;display:flex;align-items:center;justify-content:center}
.meta{left:332px;top:263px;font-size:11px;color:#555}
.meta a{color:var(--green);text-decoration:underline;font-weight:600;margin-right:6px}
.sort{left:722px;top:252px;display:flex;align-items:center;font-size:11px}
.sort .select{margin-left:10px;width:100px;height:31px;border:1px solid #ccc;border-radius:2px;display:flex;align-items:center;background:#f7f7f7}
.sort .select span{flex:1;padding-left:14px;color:#666}
.sort .select i{width:30px;height:100%;border-left:1px solid #ccc;display:flex;align-items:center;justify-content:center}

.card{left:329px;width:542px;background:#fff;border:1px solid #e0e0e0;border-radius:2px;box-shadow:0 2px 2px rgba(0,0,0,.12)}
.card .box{position:absolute;left:20px}
.price{position:absolute;left:50px;font-size:15px}
.price small{display:block;font-size:11px;margin-top:-2px}
.port{position:absolute;font-size:11px;font-weight:600;color:var(--link)}
.svc{position:absolute;font-size:11px;color:#888}
.carrier{position:absolute;display:flex;align-items:center;font-weight:600;color:#333}
.carrier i{display:inline-block;border-radius:50%;background:#333;margin-right:4px}
.carrier.sm{font-size:10px}.carrier.sm i{width:14px;height:14px}
.carrier.lg{font-size:18px}.carrier.lg i{width:32px;height:32px;margin-right:8px}
.tools{position:absolute;left:455px;display:flex;gap:6px}
.tools svg{width:17px;height:17px}
.divider{position:absolute;left:24px;right:16px;border-top:1px solid #e2e2e2}

.btn-manual{left:890px;top:206px;width:220px;height:40px;background:var(--green);color:#fff;font-size:15px;font-weight:600;border-radius:2px;display:flex;align-items:center;justify-content:center}
.side{left:889px;width:222px}
.side h4{font-size:11.5px;font-weight:400;padding:16px 20px 11px;border-bottom:1px solid #d6d6d6}
.avg li{list-style:none;display:flex;align-items:center;font-size:11px;font-weight:600;color:var(--link);height:28px;padding-left:20px}
.avg li svg{width:12px;height:12px;margin-right:11px}
.arch{padding:0 16px}
.arch .row{padding:16px 0 12px;font-size:11px}
.arch .row + .row{border-top:1px solid #d6d6d6}
.arch .line{display:flex;justify-content:space-between;margin-bottom:7px}
.arch .line a{font-weight:600}
.arch .line a.dup{text-decoration:underline}

.footer{left:0;top:1163px;width:1280px;height:60px;background:var(--footer)}
.footer nav{position:absolute;left:171px;top:23px;font-size:11px;display:flex;gap:18px}
.footer nav a{color:#999}
.social{position:absolute;left:886px;top:14px;display:flex;gap:16px}
.social span{width:32px;height:32px;border-radius:50%;background:#5d6164}
</style>
</head>
<body>
<svg width="0" height="0" style="position:absolute">
  <defs>
    <symbol id="i-search" viewBox="0 0 16 16"><circle cx="6.5" cy="6.5" r="4.8" fill="none" stroke="#b5b5b5" stroke-width="2"/><path d="M10 10l4.5 4.5" stroke="#b5b5b5" stroke-width="2.4" stroke-linecap="round"/></symbol>
    <symbol id="i-trash" viewBox="0 0 16 16"><path d="M3 4h10M6 4V2.5h4V4" stroke="#b5b5b5" stroke-width="1.4" fill="none"/><path d="M4 5h8l-.7 9H4.7z" fill="none" stroke="#b5b5b5" stroke-width="1.4"/><path d="M7 7v5M9 7v5" stroke="#b5b5b5"/></symbol>
    <symbol id="i-save" viewBox="0 0 16 16"><path d="M2 2h10l2 2v10H2z" fill="none" stroke="#b5b5b5" stroke-width="1.5"/><rect x="5" y="2.5" width="5" height="3.5" fill="#b5b5b5"/><rect x="4.5" y="9" width="7" height="4" fill="#b5b5b5"/></symbol>
    <symbol id="i-tick" viewBox="0 0 12 12"><path d="M2 6.5l2.5 2.5L10 3" fill="none" stroke="#555" stroke-width="1.6"/></symbol>
  </defs>
</svg>

<div class="stage">
  <div class="abs topbar">
    <span style="left:880px">Username &#9679;</span>
    <span style="left:976px">USD &#9662;</span>
    <span style="left:1047px">English &#9662;</span>
  </div>

  <header class="abs header">
    <div class="abs brand">LOGO</div>
    <nav class="abs menu">
      <a class="active">Menu 1</a><a>Menu 2</a><a>Menu 3</a><a>Menu 4</a><a>Menu 5</a>
    </nav>
  </header>

  <section class="abs panel formbar">
    <div class="field" style="left:22px"><b>Unit</b><small>Details..</small></div>
    <div class="field sep" style="left:138px"><b>From</b><small>Shipping Address or Port..</small></div>
    <div class="field sep" style="left:342px"><b>To</b><small>Shipping Address or Port..</small></div>
    <div class="field sep" style="left:562px"><b>Customer</b><small>Unit</small></div>
    <div class="btn-change">Change</div>
  </section>

  <aside class="abs panel filters">
    <h3>Filter 1</h3>
    <div class="check"><span class="box"></span>One</div>
    <div class="check"><span class="box"></span>Two</div>
    <div class="check"><span class="box on"><svg width="11" height="11"><use href="#i-tick"/></svg></span>Three</div>
    <hr>
    <h3>Filter 2</h3>
    <div class="check"><span class="box"></span>One</div>
    <div class="check"><span class="box"></span>Two</div>
    <div class="check"><span class="box on"><svg width="11" height="11"><use href="#i-tick"/></svg></span>Three</div>
    <hr>
    <h3>Range Filter</h3>
    <div class="range"><div class="track"></div><div class="fill"></div><div class="knob" style="left:13px"></div><div class="knob" style="left:72px"></div></div>
    <div class="range-labels"><span>Value</span><span>Value</span></div>
  </aside>

  <div class="abs btn-send">Preview and Send Selected Quotes &#10140;</div>
  <div class="abs meta"><a>Select All</a>(3) Results Found</div>
  <div class="abs sort">Sort By<div class="select"><span>Nearest</span><i><svg width="8" height="5"><path d="M0 0h8L4 5z" fill="#555"/></svg></i></div></div>

  <!-- expanded result -->
  <article class="abs card" style="top:293px;height:210px">
    <span class="box" style="top:14px"></span>
    <div class="price" style="top:12px">USD 188,458 / 36 hours</div>
    <div class="svc" style="left:410px;top:15px;color:#555">Valid Until Mar. 5, 2014</div>
    <div class="divider" style="top:40px"></div>
    <span class="port" style="left:25px;top:63px">Port Code</span><span class="svc" style="left:85px;top:63px">&gt;</span><span class="port" style="left:103px;top:63px">Port Code</span>
    <div class="carrier lg" style="left:190px;top:53px"><i></i>Harborline</div>
    <span class="svc" style="left:374px;top:63px">Service Level</span><span class="port" style="left:468px;top:63px">Price Link</span>
    <div class="divider" style="top:97px"></div>
    <span class="port" style="left:25px;top:126px">Port Code</span><span class="svc" style="left:85px;top:126px">&gt;</span><span class="port" style="left:103px;top:126px">Port Code</span>
    <div class="carrier lg" style="left:190px;top:116px"><i></i>Harborline</div>
    <span class="svc" style="left:374px;top:126px">Service Level</span><span class="port" style="left:468px;top:126px">Price Link</span>
    <div class="divider" style="top:160px"></div>
    <div class="tools" style="top:177px"><svg><use href="#i-search"/></svg><svg><use href="#i-trash"/></svg><svg><use href="#i-save"/></svg></div>
  </article>

  <article class="abs card" style="top:520px;height:70px"><span class="box" style="top:22px"></span><div class="price" style="top:19px">USD 188,458<small>36 hours</small></div><span class="port" style="left:160px;top:20px">Port Code</span><div class="carrier sm" style="left:222px;top:20px"><i></i>Harborline</div><span class="port" style="left:298px;top:20px">Port Code</span><span class="svc" style="left:367px;top:20px">Service Level</span><div class="tools" style="top:21px"><svg><use href="#i-search"/></svg><svg><use href="#i-trash"/></svg><svg><use href="#i-save"/></svg></div></article>
  <article class="abs card" style="top:607px;height:70px"><span class="box" style="top:22px"></span><div class="price" style="top:19px">USD 188,458<small>36 hours</small></div><span class="port" style="left:160px;top:20px">Port Code</span><div class="carrier sm" style="left:222px;top:20px"><i></i>Harborline</div><span class="port" style="left:298px;top:20px">Port Code</span><span class="svc" style="left:367px;top:20px">Service Level</span><div class="tools" style="top:21px"><svg><use href="#i-search"/></svg><svg><use href="#i-trash"/></svg><svg><use href="#i-save"/></svg></div></article>
  <article class="abs card" style="top:697px;height:70px"><span class="box" style="top:22px"></span><div class="price" style="top:19px">USD 188,458<small>36 hours</small></div><span class="port" style="left:160px;top:20px">Port Code</span><div class="carrier sm" style="left:222px;top:20px"><i></i>Harborline</div><span class="port" style="left:298px;top:20px">Port Code</span><span class="svc" style="left:367px;top:20px">Service Level</span><div class="tools" style="top:21px"><svg><use href="#i-search"/></svg><svg><use href="#i-trash"/></svg><svg><use href="#i-save"/></svg></div></article>
  <article class="abs card" style="top:784px;height:70px"><span class="box" style="top:22px"></span><div class="price" style="top:19px">USD 188,458<small>36 hours</small></div><span class="port" style="left:160px;top:20px">Port Code</span><div class="carrier sm" style="left:222px;top:20px"><i></i>Harborline</div><span class="port" style="left:298px;top:20px">Port Code</span><span class="svc" style="left:367px;top:20px">Service Level</span><div class="tools" style="top:21px"><svg><use href="#i-search"/></svg><svg><use href="#i-trash"/></svg><svg><use href="#i-save"/></svg></div></article>
  <article class="abs card" style="top:871px;height:70px"><span class="box" style="top:22px"></span><div class="price" style="top:19px">USD 188,458<small>36 hours</small></div><span class="port" style="left:160px;top:20px">Port Code</span><div class="carrier sm" style="left:222px;top:20px"><i></i>Harborline</div><span class="port" style="left:298px;top:20px">Port Code</span><span class="svc" style="left:367px;top:20px">Service Level</span><div class="tools" style="top:21px"><svg><use href="#i-search"/></svg><svg><use href="#i-trash"/></svg><svg><use href="#i-save"/></svg></div></article>
  <article class="abs card" style="top:961px;height:70px"><span class="box" style="top:22px"></span><div class="price" style="top:19px">USD 188,458<small>36 hours</small></div><span class="port" style="left:160px;top:20px">Port Code</span><div class="carrier sm" style="left:222px;top:20px"><i></i>Harborline</div><span class="port" style="left:298px;top:20px">Port Code</span><span class="svc" style="left:367px;top:20px">Service Level</span><div class="tools" style="top:21px"><svg><use href="#i-search"/></svg><svg><use href="#i-trash"/></svg><svg><use href="#i-save"/></svg></div></article>
  <article class="abs card" style="top:1048px;height:70px"><span class="box" style="top:22px"></span><div class="price" style="top:19px">USD 188,458<small>36 hours</small></div><span class="port" style="left:160px;top:20px">Port Code</span><div class="carrier sm" style="left:222px;top:20px"><i></i>Harborline</div><span class="port" style="left:298px;top:20px">Port Code</span><span class="svc" style="left:367px;top:20px">Service Level</span><div class="tools" style="top:21px"><svg><use href="#i-search"/></svg><svg><use href="#i-trash"/></svg><svg><use href="#i-save"/></svg></div></article>

  <div class="abs btn-manual">Create Manual Quote &nbsp;&nbsp;&#9662;</div>

  <section class="abs panel side" style="top:260px;height:156px">
    <h4>Average Prices in Market</h4>
    <ul class="avg" style="padding-top:14px">
      <li><svg viewBox="0 0 12 12"><rect x="0" y="3" width="7" height="5" fill="#222"/><path d="M7 4.5h3l2 2V8H7z" fill="#222"/><circle cx="2.5" cy="9" r="1.4" fill="#222"/><circle cx="9.5" cy="9" r="1.4" fill="#222"/></svg>USD 188,458 / 100 KG</li>
      <li><svg viewBox="0 0 12 12"><path d="M6 0.5l1 0 0 4.5 5 2.5v1.2l-5-1.2v2.7l1.5 1.2v.9L6 11.5 3.5 12v-.9L5 9.9V7.2L0 8.4V7.2l5-2.5V.5z" fill="#222" transform="rotate(45 6 6)"/></svg>USD 188,458 / 100 KG</li>
      <li><svg viewBox="0 0 12 12"><rect x="3.5" y="0.5" width="5" height="4" fill="#222"/><path d="M1 5h10l-1.5 5h-7z" fill="#222"/><path d="M0 11.5h12" stroke="#222"/></svg>USD 188,458 / 100 KG</li>
    </ul>
  </section>

  <section class="abs panel side" style="top:435px;height:177px">
    <h4>Similar results from archive</h4>
    <div class="arch">
      <div class="row"><div class="line"><span>#7G34K</span><span>Mar. 5, 2014</span></div><div class="line"><a>USD 188,458 / 100 KG</a><a class="dup">Duplicate</a></div></div>
      <div class="row"><div class="line"><span>#7G34K</span><span>Mar. 5, 2014</span></div><div class="line"><a>USD 188,458 / 100 KG</a><a class="dup">Duplicate</a></div></div>
    </div>
  </section>

  <footer class="abs footer">
    <nav><a>About Us</a><a>Privacy Policy</a><a>Terms of Services</a><a>News</a></nav>
    <div class="social" aria-label="Social links">
      <span role="img" aria-label="Social network link"></span>
      <span role="img" aria-label="Social network link"></span>
      <span role="img" aria-label="Social network link"></span>
      <span role="img" aria-label="News feed link"></span>
      <span role="img" aria-label="Video channel link"></span>
    </div>
  </footer>
</div>
</body>
</html>
```